1/4 page magazine ad

We would like a 1/4 ad in a magazine advertising a doctor in our practice. Dr. Clara Mendt, DC is the only Female Brinley Certified chiropractor in Williamsburg, VA. We would like the ad to include a large eye catching picture of a woman's pregnant belly, as the Brinley technique is for pregnant women. Please take a look at our previous ad that we have had done to see some of the elements that we liked in our other ad.

```html
<!DOCTYPE html>
<html lang="en">
<head>
<meta charset="utf-8">
<title>Dr. Clara Mendt, DC – Quarter Page Ad</title>
<link href="https://fonts.googleapis.com/css2?family=Oswald:wght@500;600;700&family=Arimo:wght@400&display=swap" rel="stylesheet">
<style>
  :root {
    --backdrop: #242424;
    --paper: #ffffff;
    --maroon: #800000;
    --gold: #f9bd16;
    --ink: #161616;
    --logo-grey: #7a7a7a;
    --white: #ffffff;
    --skin-light: #f6e2d8;
    --skin: #efc9b8;
    --top-white: #f2f3f6;
  }
  * { margin: 0; padding: 0; box-sizing: border-box; }
  html, body { width: 1200px; height: 1200px; overflow: hidden; background: var(--backdrop); }
  .ad {
    position: absolute; left: 171px; top: 66px;
    width: 857px; height: 1068px;
    background: var(--paper); overflow: hidden;
    box-shadow: 0 6px 24px rgba(0,0,0,.45);
    font-family: "Arimo", Arial, sans-serif;
  }
  .belly-photo {
    position: absolute; left: 494px; top: 0; width: 363px; height: 965px;
    background: linear-gradient(180deg, var(--skin-light) 0%, var(--top-white) 25%, var(--skin-light) 45%, var(--skin) 70%, var(--skin-light) 88%, var(--top-white) 100%);
  }
  .brand { position: absolute; left: 56px; top: 56px; display: flex; align-items: center; gap: 14px; height: 118px; }
  .brand-square { width: 108px; height: 118px; background: var(--logo-grey); }
  .brand-name {
    font-family: "Oswald", sans-serif; font-weight: 600; color: var(--maroon);
    font-size: 43px; line-height: 1.12; letter-spacing: 1px; text-transform: uppercase;
  }
  .doctor-band { position: absolute; left: 0; top: 251px; width: 612px; height: 153px; background: var(--maroon); }
  .doctor-portrait {
    position: absolute; left: 51px; top: 224px; width: 163px; height: 207px;
    background: linear-gradient(160deg, #6f8a4a 0%, #4d5e33 45%, #2a3550 100%);
    border: 3px solid #6d6d6d;
  }
  .doctor-name {
    position: absolute; left: 223px; top: 270px;
    font-family: "Oswald", sans-serif; font-weight: 600; font-size: 47px; line-height: 1;
    color: var(--white); white-space: nowrap;
  }
  .doctor-rule { position: absolute; left: 223px; top: 337px; width: 362px; height: 2px; background: var(--gold); }
  .doctor-title {
    position: absolute; left: 223px; top: 349px;
    font-family: "Oswald", sans-serif; font-weight: 500; font-size: 29px; line-height: 1;
    color: var(--white); white-space: nowrap;
  }
  .intro { position: absolute; left: 53px; top: 444px; font-size: 24px; line-height: 35px; color: var(--ink); }
  .specialty-heading {
    position: absolute; left: 53px; top: 520px;
    font-family: "Oswald", sans-serif; font-weight: 700; font-size: 40px; line-height: 1; color: var(--maroon);
  }
  .specialty-rule { position: absolute; left: 53px; top: 586px; width: 447px; height: 2px; background: var(--gold); }
  .specialty-list { position: absolute; left: 53px; top: 600px; list-style: none; font-size: 24px; line-height: 36px; color: var(--ink); }
  .specialty-list li { position: relative; padding-left: 41px; margin-bottom: 5px; }
  .specialty-list li::before {
    content: ""; position: absolute; left: 4px; top: 12px; width: 13px; height: 13px;
    border-radius: 50%; background: var(--maroon);
  }
  .phone-band {
    position: absolute; left: 0; top: 806px; width: 530px; height: 67px; background: var(--gold);
    display: flex; align-items: center; padding-left: 53px; gap: 18px;
  }
  .phone-icon { width: 50px; height: 50px; }
  .phone-number { font-family: "Oswald", sans-serif; font-weight: 700; font-size: 56px; line-height: 1; color: var(--ink); }
  .address { position: absolute; left: 53px; top: 890px; font-size: 24px; line-height: 36px; color: var(--maroon); }
  .footer-band {
    position: absolute; left: 0; top: 965px; width: 857px; height: 103px; background: var(--maroon);
    display: flex; justify-content: center; padding-top: 16px;
  }
  .website { font-size: 29px; letter-spacing: 4px; color: var(--white); font-family: "Arimo", Arial, sans-serif; }
  .website strong { color: var(--gold); font-weight: 400; }
</style>
</head>
<body>
  <div class="ad">
    <div class="belly-photo" role="img" aria-label="Photo of a pregnant woman in a white top cradling her bare belly with both hands"></div>

    <div class="brand">
      <div class="brand-square"></div>
      <div class="brand-name">Colonial Spine<br>&amp; Posture Center</div>
    </div>

    <div class="doctor-band"></div>
    <div class="doctor-portrait" role="img" aria-label="Portrait photo of Dr. Clara Mendt"></div>
    <div class="doctor-name">Dr. Clara Mendt, DC</div>
    <div class="doctor-rule"></div>
    <div class="doctor-title">Brinley Certified Chiropractor</div>

    <p class="intro">The only Female Brinley Certified<br>chiropractor in Williamsburg, VA.</p>

    <h2 class="specialty-heading">Specialty:</h2>
    <div class="specialty-rule"></div>
    <ul class="specialty-list">
      <li>Utilizing activator technique</li>
      <li>Manual adjusting</li>
      <li>Soft tissue mobilization</li>
      <li>Brinley technique for<br>well-rounded patient care</li>
    </ul>

    <div class="phone-band">
      <svg class="phone-icon" viewBox="0 0 50 50" aria-hidden="true">
        <path d="M12 6 L19 14 L15 20 C17 26 22 31 28 34 L34 29 L43 36 L38 44 C22 44 6 28 5 12 Z" fill="#161616"/>
        <path d="M27 14 A10 10 0 0 1 36 23" stroke="#161616" stroke-width="3" fill="none" stroke-linecap="round"/>
        <path d="M28 7 A17 17 0 0 1 43 22" stroke="#161616" stroke-width="3" fill="none" stroke-linecap="round"/>
      </svg>
      <span class="phone-number">757-555-0148</span>
    </div>

    <p class="address">2150 Linden Hollow Road, # 104,<br>Williamsburg, VA 23188</p>

    <div class="footer-band">
      <span class="website">www.<strong>colonialspineposture</strong>.com</span>
    </div>
  </div>
</body>
</html>
```